Cyber Security Site Design (Products & Consulting)

I need my website redesigned to be engaging, clean, efficient and modern. My company (when its up and running) is going to be concentrated on two things: a few specific products for cyber security as well as cyber security consulting services. The background I bring to the field is having worked with small companies all the way to the largest government organizations and advising them on their security posture and how to improve it. We need the ability to add products and services easily.

For a sample product, you can use either Tarnel (http://www.tarnel-relay.org/) or Vornidex Graywell (https://www.vornidex.com/products/relay-kx-and-enhanced-safe-portal).

It will replace https://dalmorenvue.com/

Target Market(s)

Cyber Security professionals in all verticals

Coding

Coded - Design and coding required

Number of Pages Required

4 page

Font styles to use
Sans Serif

Colors
6b449b

Requirements
Must have
• Ability to easily modify
• Have main page
• Have product specific pages
• Have consulting services pages
• Have executive team information
• Clean, modern design
• Usage of the logo and its color scheme
Nice to have
• I like the idea of a left collapsed sidebar (so icons only) that can expand for text.
• I am also open to a very unique landing page, possibly a shape in the middle (hexagons maybe?) with each of the options there.
Should not have
• Nothing that looks like it came out of a hacker movie

```html
<!DOCTYPE html>
<html lang="en">
<head>
<meta charset="utf-8">
<title>Dalmoren Vue — Cyber Security Products &amp; Consulting</title>
<link rel="stylesheet" href="https://fonts.googleapis.com/css2?family=Open+Sans:wght@400;600;700&display=swap">
<style>
:root{
  --purple:#6b449b;
  --ink:#2b2b2b;
  --text:#5c5c5c;
  --muted:#7a7a7a;
  --white:#ffffff;
  --tile:#f1f1f1;
  --night-1:#0d1626;
  --night-2:#1d3550;
  --footer-1:#2f3f4f;
  --footer-2:#4d5a61;
}
*{box-sizing:border-box;margin:0;padding:0}
html,body{width:1200px;height:2848px;overflow:hidden}
body{position:relative;background:var(--white);font-family:"Open Sans",Arial,sans-serif;color:var(--ink)}

/* header */
.site-header{position:absolute;left:0;top:0;width:1200px;height:99px;background:var(--white)}
.brand{position:absolute;left:99px;top:28px;display:flex;align-items:center;gap:12px}
.brand-mark{width:40px;height:40px;background:var(--purple)}
.brand-name{font-size:26px;font-weight:600;color:var(--purple);letter-spacing:1px}
.main-nav{position:absolute;top:50px;left:0;font-size:14px;color:var(--muted)}
.main-nav span{position:absolute;white-space:nowrap}
.main-nav .active{color:var(--purple);text-decoration:underline}
.main-nav .phone{color:var(--ink);font-weight:600}
.btn-consult{position:absolute;left:950px;top:40px;width:150px;height:40px;border:2px solid var(--purple);border-radius:20px;color:var(--purple);font-size:14px;font-weight:600;display:flex;align-items:center;justify-content:center}

/* hero */
.hero{position:absolute;left:0;top:99px;width:1200px;height:600px;background:linear-gradient(160deg,var(--night-1) 0%,var(--night-2) 55%,var(--night-1) 100%)}
.hero-title{position:absolute;left:0;top:183px;width:1200px;text-align:center;color:var(--white);font-size:28px;line-height:40px;font-weight:400}
.btn-ghost{position:absolute;border:2px solid var(--white);border-radius:20px;color:var(--white);font-size:14px;font-weight:600;display:flex;align-items:center;justify-content:center}

/* service cards */
.photo{position:absolute}
.service-box{position:absolute;background:var(--white)}
.service-title{position:absolute;color:var(--purple);font-size:20px;font-weight:700;white-space:nowrap}
.service-title::after{content:"";position:absolute;left:0;bottom:-8px;width:30px;height:2px;background:var(--purple)}
.service-text{position:absolute;font-size:14px;line-height:24px;color:var(--text)}
.circle-btn{position:absolute;border-radius:50%;display:flex;align-items:center;justify-content:center}

/* about */
.about-panel{position:absolute;left:100px;top:1280px;width:500px;height:399px;background:var(--purple);color:var(--white)}
.about-panel h2{position:absolute;left:41px;top:72px;font-size:28px;font-weight:400;white-space:nowrap}
.about-panel p{position:absolute;left:41px;top:146px;width:405px;font-size:14px;line-height:24px}

/* products */
.section-title{position:absolute;left:0;top:1750px;width:1200px;text-align:center;font-size:30px;font-weight:400;color:var(--ink)}
.arrow-btn{position:absolute;top:1823px;width:48px;height:48px;border:2px solid var(--purple);border-radius:50%;display:flex;align-items:center;justify-content:center}
.product-tile{position:absolute;top:1823px;width:356px;height:200px;background:var(--tile);display:flex;flex-direction:column;align-items:center;justify-content:center}
.product-name{font-size:30px;font-weight:600;color:var(--ink)}
.product-tag{font-size:13px;color:var(--ink)}
.product-text{position:absolute;top:2046px;width:330px;font-size:14px;line-height:24px;color:var(--text)}
.btn-more{position:absolute;top:2153px;width:101px;height:38px;border-radius:19px;font-size:14px;display:flex;align-items:center;justify-content:center}
.btn-more.solid{background:var(--purple);color:var(--white)}
.btn-more.outline{border:2px solid var(--purple);color:var(--purple)}

/* footer */
.site-footer{position:absolute;left:0;top:2264px;width:1200px;height:584px;color:var(--white);background:linear-gradient(180deg,var(--footer-1),var(--footer-2) 70%,#3b4a3f)}
.contact-block{position:absolute;left:99px;top:72px}
.contact-block h3{font-size:20px;font-weight:700;white-space:nowrap}
.contact-phone{position:absolute;top:52px;left:0;font-size:30px;white-space:nowrap}
.contact-mail{position:absolute;top:94px;left:0;font-size:18px;white-space:nowrap}
.contact-address{position:absolute;top:152px;left:0;font-size:14px;line-height:30px;white-space:nowrap}
.social{position:absolute;top:372px;width:42px;height:42px;border:2px solid var(--white);border-radius:50%}
.social.filled{background:var(--white)}
.field{position:absolute;left:600px;width:500px;background:var(--tile);border-radius:8px;color:var(--ink);font-size:13px;padding:10px 20px}
.btn-submit{position:absolute;left:600px;top:373px;width:148px;height:39px;border:2px solid var(--white);border-radius:20px;font-size:14px;font-weight:600;display:flex;align-items:center;justify-content:center}
.footer-links{position:absolute;left:0;top:490px;width:1200px;text-align:center;font-size:14px}
.copyright{position:absolute;left:0;top:520px;width:1200px;text-align:center;font-size:14px}
</style>
</head>
<body>

<header class="site-header">
  <div class="brand"><span class="brand-mark"></span><span class="brand-name">DALMOREN VUE</span></div>
  <nav class="main-nav">
    <span style="left:450px">Products &amp; Services</span>
    <span class="active" style="left:619px">About</span>
    <span style="left:689px">Contact</span>
    <span class="phone" style="left:771px">Call Us. 555.01.4386</span>
  </nav>
  <div class="btn-consult">Consult Now!</div>
</header>

<section class="hero" role="img" aria-label="Dark night background with streaks of blue light">
  <h1 class="hero-title">We helping and advising your organisation<br>achieve full cyber security with our<br>products and services</h1>
  <div class="btn-ghost" style="left:500px;top:334px;width:200px;height:38px">Contact Us Today!</div>
</section>

<section class="services">
  <div class="photo" style="left:99px;top:619px;width:501px;height:401px;background:linear-gradient(135deg,#3d7f94,#8fd0dc 50%,#1f4f63)" role="img" aria-label="Tablet showing a glowing security padlock screen"></div>
  <div class="service-box" style="left:99px;top:699px;width:376px;height:321px;border-right:4px solid var(--purple)"></div>
  <h2 class="service-title" style="left:141px;top:744px">Cyber Security</h2>
  <p class="service-text" style="left:141px;top:797px;width:275px">Nemo enim ipsam voluptatem quia voluptas sit aspernatur aut odit aut fugit, sed quia consequuntur magni dolores eos qui ratione luptatem sequi nesciunt ...</p>
  <div class="circle-btn" style="left:141px;top:959px;width:41px;height:41px;background:var(--purple)">
    <svg width="18" height="18" viewBox="0 0 18 18"><circle cx="9" cy="9" r="8" fill="none" stroke="#fff" stroke-width="1.5"/><path d="M5 9h7M9 6l3 3-3 3" fill="none" stroke="#fff" stroke-width="1.5"/></svg>
  </div>

  <div class="photo" style="left:600px;top:619px;width:500px;height:401px;background:linear-gradient(135deg,#2b3a5a,#c9d3df 55%,#8e98a6)" role="img" aria-label="Two business people in suits reviewing a tablet"></div>
  <div class="service-box" style="left:600px;top:940px;width:377px;height:80px;border-right:4px solid var(--purple)"></div>
  <h2 class="service-title" style="left:640px;top:967px;font-size:19px">Cyber Security Consulting</h2>
</section>

<section class="about">
  <div class="photo" style="left:0;top:1100px;width:1200px;height:499px;background:linear-gradient(90deg,#6b4a3a,#b59a86 40%,#d9dcdf 70%,#6d7c8a)" role="img" aria-label="Team meeting around a table with laptops"></div>
  <div class="about-panel">
    <h2>Dalmoren Vue, LLC.</h2>
    <p>Dalmoren Vue, LLC. Is a company that takes its roots from the idea of providing appropriate and creative solutions for cyber security operations, development and management. We have a mission ...</p>
    <div class="btn-ghost" style="left:41px;top:281px;width:150px;height:38px;font-weight:400">About Us</div>
  </div>
</section>

<section class="products">
  <h2 class="section-title">Cyber Security Products</h2>
  <div class="arrow-btn" style="left:100px"><svg width="14" height="14" viewBox="0 0 14 14"><path d="M9 2L4 7l5 5" fill="none" stroke="#6b449b" stroke-width="2"/></svg></div>
  <div class="arrow-btn" style="left:162px"><svg width="14" height="14" viewBox="0 0 14 14"><path d="M5 2l5 5-5 5" fill="none" stroke="#6b449b" stroke-width="2"/></svg></div>

  <div class="product-tile" style="left:349px"><span class="product-name" style="font-weight:400">tarnel-relay.org</span><span class="product-tag">Optimising Web Delivery</span></div>
  <div class="product-tile" style="left:744px"><span class="product-name">Vornidex</span></div>

  <p class="product-text" style="left:349px">Lorem ipsum dolor sit amet, consectetur adipiscing elit, sed do eiusmod tempor incidi-<br>dunt ut labore et dolore ...</p>
  <p class="product-text" style="left:744px">Lorem ipsum dolor sit amet, consectetur adipiscing elit, sed do eiusmod tempor incidi-<br>dunt ut labore et dolore ...</p>
  <div class="btn-more solid" style="left:349px">More</div>
  <div class="btn-more outline" style="left:744px">More</div>
</section>

<footer class="site-footer" role="img" aria-label="City skyline and highway behind a dark blue-grey overlay">
  <div class="contact-block">
    <h3>Get in Touch</h3>
    <div class="contact-phone">Call Us. 555.01.4386</div>
    <div class="contact-mail">e. info@dalmorenvue.com</div>
    <div class="contact-address">Dalmoren Vue<br>4120 Alderbrook Lane<br>Marlow, TX 75990</div>
  </div>
  <span class="social filled" style="left:99px"></span>
  <span class="social" style="left:150px"></span>
  <span class="social" style="left:201px"></span>

  <div class="field" style="top:134px;height:38px">Enter your Name</div>
  <div class="field" style="top:193px;height:40px">Emial</div>
  <div class="field" style="top:254px;height:99px">Message</div>
  <div class="btn-submit">Submit</div>

  <div class="footer-links">Products &amp; Services &nbsp; I &nbsp; About &nbsp; I &nbsp; Cyber Security Consultation &nbsp; I &nbsp; Contact</div>
  <div class="copyright">© 2018 Dalmoren Vue.</div>
</footer>

</body>
</html>
```